Stationery design bilingual preschool
Meadowlark preschool
Stationery design bilingual preschool - Childcare
Creative Brief
Bright & Fun-filled
Marita Sundqvist
Preschool director
Lövhagsvägen 9 128 31 Skarpnäck Sweden
angsfagelforskolan@postlada.se
www.angsfagelforskolan.com
Back of the business card suppose to have the same information as the front side but on Swedish.
(Subtitle) Ängsfågel Förskola AB ( name) Marita Sundqvist (title) Förskolechef (address) Lövhagsvägen 9 128 31 Skarpnäck (phone) Tel. 08 731 94 62 (cell) Mob. 073 862 40 15 (email) angsfagelforskolan@postlada.com (web side) www.angsfagelforskolan. com
butterfly2004 butterfly2004
Dear designers, I'd like to see design drafts ideas for the following products: 1. Business card 2. Letterhead 3. Envelope 4. Folder 5. CD and CD cover 6. Email signature 7. Presentation 8.Thank you card 8. Stamp 9. T-shirt, Hoody, Winter jacket/ Rain jacket, Cap, Scarf 10. Pen 11. Meadowlark character toy Thank you, PH

```html
<!DOCTYPE html>
<html lang="en">
<head>
<meta charset="utf-8">
<title>Meadowlark Preschool – Business Card</title>
<link href="https://fonts.googleapis.com/css2?family=Arimo:wght@400;700&display=swap" rel="stylesheet">
<style>
  :root {
    --backdrop: #3a3a3a;
    --card: #ffffff;
    --green: #5aa51e;
    --green-deep: #2f8a14;
    --green-light: #8fcb2c;
    --orange: #f39200;
    --ink: #555555;
    --ink-soft: #888888;
    --art-purple: #7a3e9d;
    --art-yellow: #f6c223;
  }
  * { box-sizing: border-box; margin: 0; padding: 0; }
  html, body { width: 1200px; height: 751px; overflow: hidden; }
  body {
    background: var(--backdrop);
    font-family: "Arimo", Arial, sans-serif;
    position: relative;
  }
  .card {
    position: absolute;
    top: 216px;
    width: 492px;
    height: 283px;
    background: var(--card);
    border-radius: 14px;
    overflow: hidden;
  }
  .card--front { left: 91px; }
  .card--back { left: 619px; }

  .front-band { position: absolute; inset: 0; }

  .brand-name {
    position: absolute;
    left: 28px;
    top: 24px;
    font-weight: 700;
    font-size: 31px;
    line-height: 30px;
    color: var(--green);
  }
  .contact { position: absolute; left: 28px; top: 114px; color: var(--ink); }
  .contact__name { font-size: 15px; font-weight: 700; color: var(--green); }
  .contact__title { font-size: 11px; font-weight: 700; color: var(--orange); margin-top: 2px; }
  .contact__address { font-size: 10px; line-height: 13px; margin-top: 10px; }
  .contact__lines { list-style: none; margin-top: 9px; font-size: 10px; line-height: 14px; }
  .contact__lines li { display: flex; align-items: center; gap: 6px; }
  .contact__lines svg { width: 10px; height: 10px; flex: none; }

  .mascot-art {
    position: absolute;
    left: 290px;
    top: 14px;
    width: 180px;
    height: 196px;
    border-radius: 48% 52% 46% 54%;
    background: radial-gradient(circle at 50% 45%, var(--art-yellow) 0 24%, var(--art-purple) 25% 62%, var(--green-light) 63%);
  }
  .front-web {
    position: absolute;
    right: 24px;
    bottom: 14px;
    font-size: 11px;
    color: #ffffff;
    letter-spacing: 0.5px;
  }

  .back-brand {
    position: absolute;
    left: 0; right: 0;
    top: 96px;
    text-align: center;
  }
  .back-brand__name {
    display: inline-flex;
    align-items: center;
    gap: 10px;
    font-weight: 700;
    font-size: 28px;
    color: var(--green);
  }
  .back-brand__mark {
    width: 22px; height: 22px; border-radius: 50%;
    background: var(--art-purple);
  }
  .back-brand__tagline { font-size: 10px; color: var(--ink-soft); margin-top: 4px; }
  .back-web {
    position: absolute;
    left: 40px; right: 40px;
    top: 226px;
    display: flex;
    align-items: center;
    gap: 10px;
    font-size: 10px;
    color: var(--ink-soft);
    letter-spacing: 1px;
  }
  .back-web::before, .back-web::after {
    content: ""; flex: 1; height: 1px; background: #cccccc;
  }
</style>
</head>
<body>
  <section class="card card--front">
    <svg class="front-band" viewBox="0 0 492 283" aria-hidden="true">
      <defs>
        <linearGradient id="bandFill" x1="0" y1="0" x2="1" y2="1">
          <stop offset="0" stop-color="#7cc22a"/>
          <stop offset="1" stop-color="#2f8a14"/>
        </linearGradient>
      </defs>
      <path d="M268 0 H492 V283 H0 V274 C140 270 262 256 302 200 C328 160 305 60 268 0 Z" fill="url(#bandFill)"/>
    </svg>

    <div class="brand-name">Meadowlark<br>Preschool</div>

    <div class="contact">
      <p class="contact__name">Marita Sundqvist</p>
      <p class="contact__title">Preschool director</p>
      <p class="contact__address">Lövhagsvägen 9<br>128 31 Skarpnäck, Sweden</p>
      <ul class="contact__lines">
        <li><svg viewBox="0 0 10 10"><path d="M2 1 L4 1 L4.6 3 L3.4 3.8 C4 5.2 4.8 6 6.2 6.6 L7 5.4 L9 6 L9 8 C5 8.5 1.5 5 2 1 Z" fill="var(--green)"/></svg>46 8 731 94 62</li>
        <li><svg viewBox="0 0 10 10"><rect x="2.5" y="0.5" width="5" height="9" rx="1" fill="var(--green)"/><rect x="3.4" y="1.6" width="3.2" height="5.4" fill="#fff"/></svg>46 73 862 40 15</li>
        <li><svg viewBox="0 0 10 10"><rect x="0.5" y="2" width="9" height="6" rx="1" fill="var(--green)"/><path d="M1 2.5 L5 5.5 L9 2.5" fill="none" stroke="#fff" stroke-width="0.9"/></svg>angsfagelforskolan@postlada.se</li>
      </ul>
    </div>

    <div class="mascot-art" role="img" aria-label="Meadowlark character illustration wearing a graduation cap"></div>

    <p class="front-web">angsfagelforskolan.com</p>
  </section>

  <section class="card card--back">
    <div class="back-brand">
      <div class="back-brand__name">Meadowlark Preschool<span class="back-brand__mark"></span></div>
      <p class="back-brand__tagline">learning for life</p>
    </div>
    <p class="back-web">www.angsfagelforskolan.com</p>
  </section>
</body>
</html>
```